Business Card Design

Stronger Living Compact for the Plains is a partnership of twenty different health organisations in the western suburbs of Melbourne, working together to improve the health of the local community. The western suburbs of Melbourne is one of the fastest growing and most culturally diverse populations in Australia and its communities have some of the poorest health outcomes in Australia.
Please see location for copy of the SLCP:
http://kvrt.com.au/fileadmin/filemount/pdf_files/SLCFTP_13_FINAL_JUNE_2012.pdf

Reason: Hello. I've extended the deadline because in the brief I made a confusing mention about a logo, but I actually meant the 'Stronger Living Compact for the Plains' jpg that I had already attached. Sorry about the confusion Thanks Fiona

Hello, Thanks for the designs I have already received. I have extended the deadline because I made a confusing reference to a logo in my brief, but I was talking about the 'Stronger Living Compact for the Plains' jpg I had already attached. There is no other logo for me to provide.

Thanks, Fiona

Target Market(s)

Health and state/local government managers and CEOs

Industry/Entity Type

Health

Contact Information for Business Card

Fiona Tremblay
Executive Officer
Stronger Living Compact for the Plains
Ph: 0438 592 614
Fiona.Tremblay@qn.org.au

Requirements
Must have
• logo and details as provided.
Would prefer matt finish
I can't see that logo has successfully attached so if it has not, please email or call me to follow up.

```html
<!DOCTYPE html>
<html lang="en">
<head>
<meta charset="utf-8">
<title>Stronger Living Compact for the Plains – Business Card</title>
<link href="https://fonts.googleapis.com/css2?family=Open+Sans:wght@400;700&display=swap" rel="stylesheet">
<style>
  :root {
    --backdrop: #eceded;
    --lime: #bcd86a;
    --blue: #0089cf;
    --sky: #3bbde9;
    --coral: #ee4059;
    --white: #ffffff;
    --photo-warm: #b9a58f;
    --photo-cool: #8fa4ad;
    --photo-green: #8f9a6e;
    --photo-red: #d9344f;
    --photo-cyan: #45b8dc;
  }
  * { margin: 0; padding: 0; box-sizing: border-box; }
  html, body {
    width: 994px; height: 1200px; overflow: hidden;
    background: var(--backdrop);
    font-family: "Open Sans", Arial, sans-serif;
  }
  .card {
    position: absolute;
    border-radius: 24px;
    overflow: hidden;
    background: var(--lime);
    box-shadow: 0 6px 14px rgba(0,0,0,0.18);
  }
  .card--front { left: 83px; top: 75px; width: 819px; height: 472px; }
  .card--back  { left: 92px; top: 648px; width: 817px; height: 470px; }

  .card__field {
    position: absolute; left: 0; right: 0;
    background: var(--blue);
  }
  .card--front .card__field { top: 37px; height: 400px; }
  .card--back .card__field  { top: 37px; height: 399px; }

  .wordmark {
    position: absolute;
    color: var(--white);
    font-weight: 700;
    letter-spacing: -0.5px;
  }
  .card--front .wordmark { left: 76px; top: 48px; font-size: 54px; line-height: 61px; }
  .card--back .wordmark  { left: 612px; top: 36px; font-size: 34px; line-height: 38px; }

  .mosaic {
    position: absolute; left: 369px; top: 0;
    width: 450px; height: 400px;
    display: grid;
    grid-template-columns: 150px 150px 150px;
    grid-template-rows: repeat(4, 100px);
  }
  .tile--photo-warm  { background: linear-gradient(135deg, var(--photo-warm), #7d6d60); }
  .tile--photo-cool  { background: linear-gradient(135deg, var(--photo-cool), #5b6d76); }
  .tile--photo-green { background: linear-gradient(135deg, var(--photo-green), #5f6a45); }
  .tile--photo-red   { background: linear-gradient(135deg, var(--photo-red), #b8243d); }
  .tile--photo-cyan  { background: linear-gradient(135deg, var(--photo-cyan), #2ea3c9); }
  .tile--lime  { background: var(--lime); }
  .tile--sky   { background: var(--sky); }
  .tile--coral { background: var(--coral); }

  .contact { position: absolute; left: 100px; top: 126px; color: var(--white); }
  .contact__name { font-weight: 700; font-size: 25px; line-height: 34px; }
  .contact__role { font-size: 24px; line-height: 34px; margin-bottom: 38px; }
  .contact__line { display: flex; align-items: center; font-size: 26px; line-height: 40px; }
  .contact__icon { width: 22px; height: 22px; margin-right: 10px; }
</style>
</head>
<body>

<section class="card card--front" aria-label="Card front">
  <div class="card__field">
    <div class="wordmark">Stronger<br>Living<br>Compact<br>for the<br>Plains</div>
    <div class="mosaic">
      <div class="tile tile--photo-warm" role="img" aria-label="Photo of a researcher at a laboratory microscope"></div>
      <div class="tile tile--lime"></div>
      <div class="tile tile--photo-cool" role="img" aria-label="Photo of new suburban housing"></div>
      <div class="tile tile--photo-red" role="img" aria-label="Red-tinted photo of a community swimming pool"></div>
      <div class="tile tile--photo-warm" role="img" aria-label="Photo of a health worker with a mother and baby"></div>
      <div class="tile tile--photo-cyan" role="img" aria-label="Cyan-tinted photo of an older couple"></div>
      <div class="tile tile--sky"></div>
      <div class="tile tile--photo-warm" role="img" aria-label="Photo of a teacher with a student"></div>
      <div class="tile tile--photo-green" role="img" aria-label="Photo of older people exercising outdoors"></div>
      <div class="tile tile--photo-cool" role="img" aria-label="Photo of students in first aid training"></div>
      <div class="tile tile--photo-green" role="img" aria-label="Photo of a community garden"></div>
      <div class="tile tile--coral"></div>
    </div>
  </div>
</section>

<section class="card card--back" aria-label="Card back">
  <div class="card__field">
    <div class="contact">
      <p class="contact__name">Fiona Tremblay</p>
      <p class="contact__role">Executive Officer</p>
      <p class="contact__line">
        <svg class="contact__icon" viewBox="0 0 24 24" aria-hidden="true">
          <path d="M6.5 2.5c.8-.4 1.6 0 2 .8l1.6 3.4c.3.7.1 1.5-.5 1.9l-1.4 1c.8 2.4 2.5 4.6 4.6 6l1.2-1.2c.6-.5 1.4-.6 2-.2l3.1 2c.7.5.9 1.4.5 2.1l-1 1.6c-.6 1-1.8 1.5-2.9 1.1C9.5 19.2 4.8 13.6 3.6 7.1c-.2-1.1.3-2.2 1.3-2.8z" fill="none" stroke="#ffffff" stroke-width="1.6"/>
        </svg>
        0438 592 614
      </p>
      <p class="contact__line">
        <svg class="contact__icon" viewBox="0 0 24 24" aria-hidden="true">
          <rect x="2" y="5" width="20" height="14" fill="none" stroke="#ffffff" stroke-width="1.6"/>
          <path d="M2 5l10 8 10-8M2 19l7.5-7M22 19l-7.5-7" fill="none" stroke="#ffffff" stroke-width="1.6"/>
        </svg>
        Fiona.Tremblay@qn.org.au
      </p>
    </div>
    <div class="wordmark">Stronger<br>Living<br>Compact<br>for the<br>Plains</div>
  </div>
</section>

</body>
</html>
```